The Timber Loft

We need a business card design for our wardrobe company.
Please visit our website www.zorvelcabinets.com to get an idea of who we are.

```html
<!DOCTYPE html>
<html lang="en">
<head>
<meta charset="utf-8">
<title>The Timber Loft – Business Card</title>
<link href="https://fonts.googleapis.com/css2?family=Open+Sans:wght@300;400;600;700;800&display=swap" rel="stylesheet">
<style>
  :root {
    --backdrop: #d8d3cb;
    --card: #262626;
    --card-deep: #1c1c1c;
    --stripe: #6a6a6a;
    --stripe-light: #7a7a7a;
    --ink: #f2f2f2;
    --ink-soft: #d6d6d6;
    --dot: #121212;
  }
  * { margin: 0; padding: 0; box-sizing: border-box; }
  html, body {
    width: 1200px; height: 1023px; overflow: hidden;
    background: var(--backdrop);
    font-family: "Open Sans", Arial, sans-serif;
  }
  .card {
    position: absolute; left: 100px; top: 226px;
    width: 1000px; height: 570px;
    background: linear-gradient(160deg, var(--card) 0%, var(--card-deep) 100%);
    border-radius: 6px;
    box-shadow: 0 18px 40px rgba(0,0,0,.35);
    color: var(--ink);
    overflow: hidden;
  }
  .brand-mark {
    position: absolute; left: 44px; top: 110px;
    display: flex; align-items: center; gap: 12px;
  }
  .brand-mark__square { width: 22px; height: 22px; background: var(--ink); }
  .brand-mark__name { font-size: 20px; font-weight: 600; color: var(--ink); }
  .company { position: absolute; left: 300px; top: 72px; }
  .company__name {
    font-size: 44px; font-weight: 700; letter-spacing: .5px; text-transform: uppercase; line-height: 1.2;
  }
  .company__tagline {
    font-size: 38px; font-weight: 400; color: var(--ink-soft); margin-top: 4px; line-height: 1.2;
  }
  .stripe {
    position: absolute; left: 0; top: 230px; width: 100%; height: 78px;
    background: linear-gradient(180deg, var(--stripe-light), var(--stripe));
  }
  .person { position: absolute; left: 44px; top: 236px; line-height: 1; }
  .person__name { font-size: 44px; font-weight: 800; text-transform: uppercase; }
  .person__name span { font-weight: 300; }
  .person__role { font-size: 20px; font-weight: 700; text-transform: uppercase; margin-top: 4px; }
  .contacts { position: absolute; left: 44px; top: 350px; list-style: none; }
  .contacts li {
    display: flex; align-items: center; gap: 22px;
    font-size: 24px; color: var(--ink-soft); height: 52px;
  }
  .contacts svg { width: 28px; height: 28px; flex: none; }
  .website {
    position: absolute; left: 560px; top: 488px;
    display: flex; align-items: center; gap: 18px;
    font-size: 24px; font-weight: 700;
  }
  .website svg { width: 30px; height: 30px; }
  .social { position: absolute; right: 36px; top: 36px; display: flex; gap: 10px; }
  .social span {
    width: 32px; height: 32px; border-radius: 50%;
    background: var(--dot); box-shadow: 0 0 0 1px #3a3a3a;
  }
</style>
</head>
<body>
  <div class="card">
    <div class="brand-mark">
      <span class="brand-mark__square"></span>
      <span class="brand-mark__name">The Timber Loft</span>
    </div>

    <div class="company">
      <div class="company__name">The Timber Loft</div>
      <div class="company__tagline">Crafted to Fit Your Space</div>
    </div>

    <div class="social" aria-label="Social profiles">
      <span></span><span></span><span></span><span></span>
    </div>

    <div class="stripe"></div>
    <div class="person">
      <div class="person__name">Name <span>Here</span></div>
      <div class="person__role">Designation</div>
    </div>

    <ul class="contacts">
      <li>
        <svg viewBox="0 0 24 24" fill="none" stroke="#f2f2f2" stroke-width="2"><path d="M3 11 12 3l9 8"/><path d="M5 10v10h14V10"/><rect x="10" y="13" width="4" height="7"/></svg>
        Unit 4, 22 Harrow Lane, Leeds LS2 7QB
      </li>
      <li>
        <svg viewBox="0 0 24 24" fill="none" stroke="#f2f2f2" stroke-width="2"><circle cx="12" cy="12" r="10"/><path d="M8 7c0 5 4 9 9 9l1-2-3-1-1 1c-2-1-3-2-4-4l1-1-1-3z" fill="#f2f2f2" stroke="none"/></svg>
        0113 496 0718
      </li>
      <li>
        <svg viewBox="0 0 24 24" fill="none" stroke="#f2f2f2" stroke-width="2"><rect x="3" y="5" width="18" height="14"/><path d="M3 5l9 8 9-8"/></svg>
        info@zorvelcabinets.com
      </li>
    </ul>

    <div class="website">
      <svg viewBox="0 0 24 24" fill="none" stroke="#f2f2f2" stroke-width="1.8"><circle cx="12" cy="12" r="10" fill="#f2f2f2" stroke="none"/><g stroke="#262626"><circle cx="12" cy="12" r="7"/><ellipse cx="12" cy="12" rx="3" ry="7"/><path d="M5 12h14M6 8.5h12M6 15.5h12"/></g></svg>
      www.zorvelcabinets.com
    </div>
  </div>
</body>
</html>
```